Data Analytics Platform Website Design

Website design for a new data analytics platform called Metrica Core. I need a design that is simple but informative, professional but still sexy and that is aimed at the business professional instead of being "technical". I have a logo (picture uploaded) and also screenshots from the platform itself and I can also provide example websites from competitors that are similar in design and layout to what I need. I also have the messaging but I need help with photos, icons, font, layout, etc. I want to utilize some of the colors in the logo, but I want the overall color scheme to utilize darker blues (more serious feeling, less playful) with one accent color for highlighting. This design cannot be "fun", "playful", or "cheerful" and should instead be "professional", "serious", but still uncluttered and clean cut. However, simple does not mean easy because I want to see transitions that are clean and high level. I want the final design to be all of that while showing the company and our product as capable, serious, and reliable.

Example websites:
1. www.valdrenix.com
2. q7.ai
3. corvelane.com
4. https://www.pym.com/en_us/software/lorsa.html
5. https://www.belvoro.com/
6. gwendel.ai

Target Market(s)

Business Professionals - Government/large companies/data analytics focused

Industry/Entity Type

Data Science

Number of Pages Required

3 page

Font styles to use
Serif
Sans Serif

Requirements
Must have
• It must be clean and professional. Cannot be cluttered or too "busy". No playful or childish looks at all.
Nice to have
• I want to see professional designs but also professional concepts incorporated.
Should not have
• Should not have Comic Sans or the like, no playful or "techy" themes

```html
<!DOCTYPE html>
<html lang="en">
<head>
<meta charset="utf-8">
<title>Metrica Core — Platform</title>
<link href="https://fonts.googleapis.com/css2?family=Montserrat:wght@400;500;600;700&display=swap" rel="stylesheet">
<style>
:root{
  --blue:#1a4a94;
  --blue-dark:#0f2c5c;
  --navy:#0c2147;
  --accent:#2f78d6;
  --ink:#141a26;
  --text:#535a66;
  --hero-bg:#f1f4fa;
  --soft:#e3e9f4;
  --softer:#eef2f9;
  --white:#ffffff;
}
*{margin:0;padding:0;box-sizing:border-box}
html,body{width:1200px;height:2584px;overflow:hidden}
body{font-family:'Montserrat',sans-serif;color:var(--ink);background:var(--white);position:relative}
.abs{position:absolute}
a{color:inherit;text-decoration:none}

.topbar{top:0;left:0;width:1200px;height:56px;background:var(--white)}
.topbar .contact{top:22px;left:229px;font-size:9px;font-weight:500;display:flex;gap:20px;align-items:center}
.topbar .contact span{display:flex;align-items:center;gap:4px}
.social-top{top:22px;left:878px;display:flex;gap:16px}
.social-top i,.social-foot i{display:block;border-radius:50%;border:1.5px solid var(--ink)}
.social-top i{width:10px;height:10px}

.hero{top:56px;left:0;width:1200px;height:536px;background:var(--hero-bg);overflow:hidden}
.hero-stripe{top:0;left:0}
.hero-photo{top:90px;left:572px;width:518px;height:446px;background:linear-gradient(160deg,#d5dae3 0%,#9eabc0 45%,#2c3f63 100%);border-radius:200px 200px 0 0}
.brand{top:88px;left:231px;display:flex;align-items:center;gap:8px;font-size:19px;font-weight:500;letter-spacing:.5px;color:var(--ink)}
.brand i{width:22px;height:18px;background:var(--blue);display:block}
.nav{top:95px;left:539px;display:flex;gap:26px;font-size:9px;font-weight:600}
.nav a.active{color:var(--accent);border-bottom:2px solid var(--accent);padding-bottom:7px}
.search{top:93px;left:956px}
.hero-title{top:256px;left:229px;font-size:24px;font-weight:500;letter-spacing:-.2px;white-space:nowrap}
.hero-lead{top:303px;left:229px;font-size:10px;font-weight:600;line-height:19px;width:290px}
.hero-body{top:359px;left:229px;font-size:10px;line-height:19px;color:var(--text);width:260px}
.btn-start{top:437px;left:229px;width:128px;height:40px;border-radius:20px;background:var(--blue);color:#fff;font-size:12px;font-weight:600;display:flex;align-items:center;gap:12px;padding-left:5px}
.btn-start .ic{width:30px;height:30px;border-radius:50%;background:#fff;display:flex;align-items:center;justify-content:center}

.about{top:592px;left:0;width:1200px;height:438px;background:#f6f8fc}
.eyebrow{font-size:15px;font-weight:600;color:var(--blue)}
.subhead{font-size:11px;font-weight:500;margin-top:4px}
.about-intro{top:690px;left:229px;width:170px}
.about-intro p{font-size:8.5px;line-height:15px;color:var(--text);margin-top:13px}
.btn-more{display:inline-block;margin-top:18px;width:94px;height:29px;border-radius:15px;background:var(--blue);color:#fff;font-size:9px;font-weight:600;text-align:center;line-height:29px}
.card{top:691px;width:167px;height:239px;background:var(--white);border-radius:4px;box-shadow:0 4px 18px rgba(15,40,90,.09);padding:30px 22px}
.card.feature{background:linear-gradient(110deg,#24579f 0%,#1a4a94 55%,#143d7d 100%);color:#fff}
.card h3{font-size:12.5px;font-weight:500;line-height:15px;margin-top:20px;height:36px}
.card p{font-size:8px;line-height:15px;color:var(--text);margin-top:14px}
.card.feature p{color:#fff}
.card .arrow{position:absolute;left:22px;bottom:14px}

.why{top:1030px;left:0;width:1200px;height:450px;overflow:hidden}
.video{top:1135px;left:229px;width:385px;height:238px;border-radius:4px;background:linear-gradient(120deg,#c9ccd0 0%,#8f949b 40%,#26324a 75%,#141f36 100%)}
.play{top:1236px;left:402px;width:40px;height:40px;border-radius:50%;background:var(--blue);display:flex;align-items:center;justify-content:center}
.why-text{top:1138px;left:652px;width:320px}
.why-item{display:flex;gap:16px;margin-top:28px}
.why-item:first-of-type{margin-top:24px}
.why-item h4{font-size:10px;font-weight:500;color:var(--accent)}
.why-item p{font-size:8.5px;line-height:15px;color:var(--text);margin-top:3px}

.projects-head{top:1566px;left:229px}
.see-all{top:1590px;left:871px;font-size:11px;display:flex;gap:8px;align-items:center}
.project{top:1636px;width:233px}
.project .img{height:150px;border-radius:3px}
.project h4{font-size:10px;font-weight:600;margin:15px 10px 0}
.project p{font-size:8.5px;line-height:15px;color:var(--text);margin:4px 10px 0}
.dots{top:1906px;left:571px;display:flex;gap:16px;align-items:center}
.dots i{display:block;width:10px;height:10px;border-radius:50%;border:1.3px solid #555}
.dots i.on{width:6px;height:6px;background:var(--blue);border:none}

.clients-head{top:1988px;left:229px}
.clients{top:2066px;left:229px;width:740px;display:flex;justify-content:space-between}
.clients span{width:120px;text-align:center;font-size:12px;font-weight:600;color:#a4aab3;line-height:26px;white-space:nowrap}

.footer{top:2194px;left:0;width:1200px;height:325px;background:linear-gradient(180deg,var(--blue) 0%,var(--navy) 100%);color:#fff}
.fcol{top:2291px}
.fcol h5{font-size:11px;font-weight:500;margin-bottom:22px}
.fcol li{list-style:none;font-size:8.5px;line-height:19px}
.social-foot{top:2382px;left:837px;display:flex;gap:28px}
.social-foot i{width:14px;height:14px;border-color:#fff}
.copy{top:2546px;left:0;width:1200px;text-align:center;font-size:9px}
</style>
</head>
<body>

<div class="abs topbar">
  <div class="abs contact">
    <span><svg width="9" height="9" viewBox="0 0 10 10"><path d="M2 1l2 2-1 1.5a5 5 0 0 0 2.5 2.5L7 6l2 2-1.5 1.5C4 9 1 6 .5 2.5Z" fill="none" stroke="#141a26"/></svg>(555) 204 7731</span>
    <span><svg width="10" height="8" viewBox="0 0 10 8"><rect x=".5" y=".5" width="9" height="7" fill="none" stroke="#141a26"/><path d="M.5.5 5 4.5 9.5.5" fill="none" stroke="#141a26"/></svg>GET QUOTE</span>
  </div>
  <div class="abs social-top"><i></i><i></i><i></i><i></i></div>
</div>

<section class="abs hero">
  <svg class="abs hero-stripe" width="1200" height="536" viewBox="0 0 1200 536">
    <defs><linearGradient id="stripe" x1="0" y1="0" x2="0" y2="1"><stop offset="0" stop-color="#5f86c2"/><stop offset="1" stop-color="#143d7d"/></linearGradient></defs>
    <polygon points="1128,-56 1200,-56 1200,536 890,536" fill="url(#stripe)"/>
  </svg>
  <div class="abs hero-photo" role="img" aria-label="Photo of three smiling business colleagues looking at a tablet together"></div>
</section>
<div class="abs brand"><i></i>Metrica Core</div>
<nav class="abs nav">
  <a class="active">HOME</a><a>PLATFORM</a><a>SOLUTIONS</a><a>LEARN</a><a>CUSTOMERS</a><a>COMPANY</a>
</nav>
<svg class="abs search" width="12" height="12" viewBox="0 0 12 12"><circle cx="5" cy="5" r="3.8" fill="none" stroke="#141a26" stroke-width="1.8"/><path d="M8 8l3 3" stroke="#141a26" stroke-width="2"/></svg>
<h1 class="abs hero-title">METRICA CORE PLATFORM</h1>
<p class="abs hero-lead">Lorem ipsum dolor sit amet, consectetur adipiscing elit, sed do eiusmod tempor incididunt ut labore</p>
<p class="abs hero-body">Duis aute irure dolor in reprehenderit in voluptate velit esse cillum dolore eu fugiat nulla pariatur. Excepteur sint occaecat cupidatat non proident,</p>
<a class="abs btn-start"><span class="ic"><svg width="14" height="16" viewBox="0 0 14 16"><path d="M8 1 2 9h5l-1 6 6-8H7Z" fill="none" stroke="#1a4a94" stroke-width="1.5" stroke-linejoin="round"/></svg></span>Get Started</a>

<section class="abs about"></section>
<div class="abs about-intro">
  <div class="eyebrow">SHORT ABOUT US</div>
  <div class="subhead">Built for Any Size Business</div>
  <p>Sed ut perspiciatis unde omnis iste natus error sit voluptatem accusantium doloremque laudantium, totam rem aperiam, eaque ipsa quae</p>
  <p style="margin-top:15px">ab illo inventore veritatis et quasi architecto beatae vitae dicta sunt explicabo. Nemo enim ipsam</p>
  <a class="btn-more">Learn More</a>
</div>

<div class="abs card feature" style="left:427px">
  <svg width="34" height="38" viewBox="0 0 34 38" fill="none" stroke="#fff" stroke-width="1.6"><rect x="4" y="32" width="26" height="4"/><path d="M8 32V26h18v6M12 26l-4-14 6-8 5 4-5 6 6 12"/><circle cx="22" cy="18" r="3"/></svg>
  <h3>Intelligent Observability</h3>
  <p>See it all in-context, including metrics, logs, traces, entity relationships, UX, behavior, and vulnerability scores</p>
  <svg class="arrow" width="12" height="8" viewBox="0 0 12 8"><path d="M0 4h11M8 1l3 3-3 3" fill="none" stroke="#fff"/></svg>
</div>
<div class="abs card" style="left:613px">
  <svg width="34" height="38" viewBox="0 0 34 38" fill="none" stroke="#1a4a94" stroke-width="1.6"><path d="M10 4h14v6h5v18h-5v6H10v-6H5V10h5Z"/><circle cx="17" cy="19" r="5"/><path d="M17 4v10M17 24v10M5 19h7M22 19h7"/></svg>
  <h3>Artificial intelligence Assistance</h3>
  <p>Free your time with precise answers for proactive problem resolution and performance improvements.</p>
  <svg class="arrow" width="12" height="8" viewBox="0 0 12 8"><path d="M0 4h11M8 1l3 3-3 3" fill="none" stroke="#141a26"/></svg>
</div>
<div class="abs card" style="left:799px">
  <svg width="40" height="38" viewBox="0 0 40 38" fill="none" stroke="#1a4a94" stroke-width="1.6"><rect x="2" y="24" width="5" height="12" rx="2"/><rect x="12" y="20" width="5" height="16" rx="2"/><rect x="22" y="22" width="5" height="14" rx="2"/><rect x="32" y="12" width="5" height="24" rx="2"/><path d="M4 14l10-4 10 4 12-10"/></svg>
  <h3>User Experience &amp; Business Analytics</h3>
  <p>Eliminate silos and accelerate teamwork with a single source of truth for your Biz, Dev, Sec and Ops teams.</p>
  <svg class="arrow" width="12" height="8" viewBox="0 0 12 8"><path d="M0 4h11M8 1l3 3-3 3" fill="none" stroke="#141a26"/></svg>
</div>

<section class="abs why">
  <svg width="1200" height="450" viewBox="0 0 1200 450">
    <polygon points="120,0 467,0 300,450 0,450 0,330" fill="#eef2f9"/>
    <polygon points="182,0 467,0 300,450 15,450" fill="#e3e9f4"/>
  </svg>
</section>
<div class="abs video" role="img" aria-label="Photo of a man working on a laptop showing the analytics dashboard"></div>
<div class="abs play"><svg width="12" height="14" viewBox="0 0 12 14"><path d="M1 1l10 6-10 6Z" fill="#fff"/></svg></div>
<div class="abs why-text">
  <div class="eyebrow">WHY CHOOSE US</div>
  <div class="subhead">Excepteur sint occaecat cupidatat non proident.</div>
  <div class="why-item">
    <svg width="30" height="30" viewBox="0 0 30 30" fill="none" stroke="#1a4a94" stroke-width="1.3" style="flex:none"><rect x="1" y="2" width="8" height="7"/><rect x="11" y="2" width="8" height="7"/><rect x="21" y="2" width="8" height="7"/><path d="M5 9v5h10v4M25 9v5H15"/><rect x="10" y="18" width="10" height="4"/><rect x="10" y="24" width="10" height="4"/></svg>
    <div><h4>Satisfied Platform</h4><p>Neque porro quisquam est, qui dolorem ipsum quia dolor sit amet, consectetur, adipisci velit, sed quia non numquam eius modi tempora incidunt ut labore et dolore</p></div>
  </div>
  <div class="why-item">
    <svg width="30" height="30" viewBox="0 0 30 30" fill="none" stroke="#1a4a94" stroke-width="1.3" style="flex:none"><path d="M4 10l4-3 4 5-2 2a9 9 0 0 0 5 5l2-2 5 4-3 4C10 26 3 18 4 10Z"/><circle cx="22" cy="8" r="7"/><text x="17" y="10" font-size="5" fill="#1a4a94" stroke="none" font-family="Montserrat,sans-serif">24/7</text></svg>
    <div><h4>24/7 Hours Support</h4><p>Ut enim ad minima veniam, quis nostrum exercitationem ullam corporis suscipit laboriosam, nisi ut aliquid ex ea commodi consequatur?</p></div>
  </div>
</div>

<div class="abs projects-head">
  <div class="eyebrow">DISCOVER OUR LATEST PROJECTS</div>
  <div class="subhead">Get the Insight into Our Recent Work</div>
</div>
<a class="abs see-all">See All Projects <svg width="12" height="8" viewBox="0 0 12 8"><path d="M0 4h11M8 1l3 3-3 3" fill="none" stroke="#141a26"/></svg></a>
<article class="abs project" style="left:229px">
  <div class="img" role="img" aria-label="Photo of business team reviewing documents in an office" style="background:linear-gradient(135deg,#e6e9ee,#7d8fb0 60%,#1e2d50)"></div>
  <h4>Sed ut perspiciatis unde omnis iste natus</h4>
  <p>Ut enim ad minim veniam, quis nostrud exercita tion ullamco laboris nisi ut aliquip ex ea commodo consequat.</p>
</article>
<article class="abs project" style="left:485px">
  <div class="img" role="img" aria-label="Photo of a meeting at a round table with a clipboard" style="background:linear-gradient(135deg,#cfc7bd,#eceae6 50%,#9fa6b1)"></div>
  <h4 style="margin-left:14px">Architecto beatae vitae dicta sunt</h4>
  <p style="margin-left:14px">Nemo enim ipsam voluptatem quia voluptas sit aspernatur aut odit aut fugit, sed quia consequ untur magni dolores eos qui ratione</p>
</article>
<article class="abs project" style="left:740px">
  <div class="img" role="img" aria-label="Photo of a businesswoman working at a laptop in a bright office" style="background:linear-gradient(135deg,#d6cfc3,#f2efe9 50%,#c9b9a2)"></div>
  <h4 style="color:var(--accent)">Software Innovation for the new normal.</h4>
  <p>Lorem ipsum dolor sit amet, consectetur adipis cing elit, sed do eiusmod tempor incididunt ut labore et dolore magna aliqua</p>
</article>
<div class="abs dots"><i class="on"></i><i></i><i></i></div>

<div class="abs clients-head">
  <div class="eyebrow">OUR CLIENTS</div>
  <div class="subhead">Trusted by Thousands of Diverse Companies</div>
</div>
<div class="abs clients">
  <span>Purelane</span><span>Designworks</span><span>Mosaic Studio</span><span>Handcraft Co</span><span>Barberline</span>
</div>

<footer class="abs footer"></footer>
<div class="abs fcol" style="left:229px;color:#fff">
  <h5>OFFICE</h5>
  <ul><li>18 Harlow Lane, Leeds</li><li>LS1 4QT</li><li>info@metricacore.com</li><li>+44 113 555 0192</li></ul>
</div>
<div class="abs fcol" style="left:461px;color:#fff">
  <h5>HELP</h5>
  <ul><li>FAQ's</li><li>Term &amp; Conditions</li><li>Privacy Policy</li><li>Help</li><li>Services</li></ul>
</div>
<div class="abs fcol" style="left:663px;color:#fff">
  <h5>QUICK LINKS</h5>
  <ul><li>About</li><li>Contact</li><li>Career</li><li>Blog</li></ul>
</div>
<div class="abs fcol" style="left:837px;color:#fff">
  <h5>OPENING TIME</h5>
  <ul><li>Mon - Fri : 7.00 am - 09.00 pm</li></ul>
</div>
<div class="abs social-foot"><i></i><i></i><i></i><i></i></div>
<div class="abs copy">Copyright © 2021</div>

</body>
</html>
```